Best in class business looking for best in class stationery that accurately reflects the brand image we are trying to build as the brand expands throughout the country. The Varying items should be an eye catching design that makes even the simplest letter or small business card stand out in the crowd.

Target Market(s)

Professionals

Industry/Entity Type

Real Estate

Other font styles liked:
• See atttached logo

Requirements
Must have
• Letterhead
• Business cards
• Envelopes
• Labels for larger mailings
Nice to have
• Folders
• Notebook
Should not have
• Stale design elements

```html
<!DOCTYPE html>
<html lang="en">
<head>
<meta charset="utf-8">
<title>Ridgeline Property Group – Business Cards</title>
<link rel="stylesheet" href="https://fonts.googleapis.com/css2?family=Oswald:wght@500&family=Open+Sans:wght@400;600&display=swap">
<style>
  :root {
    --backdrop: #2b2b2b;
    --card: #1c1c1d;
    --brand-blue: #2f4aa8;
    --accent-blue: #1f8fd6;
    --ink-light: #f2f2f2;
    --divider: #cfcfcf;
  }
  * { box-sizing: border-box; margin: 0; padding: 0; }
  html, body { width: 1200px; height: 750px; overflow: hidden; }
  body {
    background: var(--backdrop);
    font-family: "Open Sans", Arial, sans-serif;
    position: relative;
  }
  .card {
    position: absolute;
    width: 520px;
    height: 297px;
    background: var(--card);
    box-shadow: 0 10px 28px rgba(0,0,0,0.45);
  }
  .card--front { left: 600px; top: 55px; }
  .card--back { left: 170px; top: 395px; }

  /* Front: company name */
  .brand {
    position: absolute;
    inset: 0;
    display: flex;
    align-items: center;
    justify-content: center;
    gap: 14px;
  }
  .brand__square {
    width: 22px;
    height: 22px;
    background: var(--brand-blue);
  }
  .brand__name {
    font-family: "Open Sans", Arial, sans-serif;
    font-weight: 600;
    font-size: 27px;
    letter-spacing: 1px;
    color: var(--brand-blue);
    text-transform: uppercase;
  }

  /* Back: contact details */
  .identity {
    position: absolute;
    right: 290px;
    top: 100px;
    text-align: right;
  }
  .identity__name {
    font-family: "Oswald", Arial, sans-serif;
    font-weight: 500;
    font-size: 30px;
    line-height: 1.1;
    color: var(--ink-light);
    letter-spacing: 0.5px;
  }
  .identity__title {
    font-size: 14px;
    color: var(--accent-blue);
  }
  .divider {
    position: absolute;
    left: 248px;
    top: 96px;
    width: 1px;
    height: 78px;
    background: var(--divider);
  }
  .contact {
    position: absolute;
    left: 264px;
    top: 98px;
    list-style: none;
  }
  .contact__item {
    display: flex;
    align-items: center;
    gap: 7px;
    font-size: 14px;
    line-height: 19px;
    color: var(--ink-light);
  }
  .contact__icon {
    width: 12px;
    height: 12px;
    flex: none;
    fill: var(--accent-blue);
  }
  .address {
    position: absolute;
    left: 42px;
    bottom: 34px;
    font-size: 14px;
    color: var(--ink-light);
  }
  .address__company { color: var(--accent-blue); }
</style>
</head>
<body>
  <section class="card card--front" aria-label="Business card front">
    <div class="brand">
      <span class="brand__square"></span>
      <span class="brand__name">Ridgeline Property Group</span>
    </div>
  </section>

  <section class="card card--back" aria-label="Business card back">
    <div class="identity">
      <p class="identity__name">JOHN SMITH</p>
      <p class="identity__title">Managing Director</p>
    </div>
    <span class="divider"></span>
    <ul class="contact">
      <li class="contact__item">
        <svg class="contact__icon" viewBox="0 0 12 12"><path d="M2.5 0.5l2 2.2-1.1 1.2c0.7 1.5 1.9 2.8 3.5 3.6l1.2-1.1 2.4 1.9-1.3 2.1C5 10.2 1.6 6.8 1.1 2.2z"/></svg>
        <span>123 456 7890</span>
      </li>
      <li class="contact__item">
        <svg class="contact__icon" viewBox="0 0 12 12"><path d="M3 0h6a1 1 0 0 1 1 1v10a1 1 0 0 1-1 1H3a1 1 0 0 1-1-1V1a1 1 0 0 1 1-1zm0.5 1.5v7.5h5V1.5zM6 9.7a0.7 0.7 0 1 0 0 1.4a0.7 0.7 0 1 0 0-1.4z"/></svg>
        <span>123 456 7890</span>
      </li>
      <li class="contact__item">
        <svg class="contact__icon" viewBox="0 0 12 12"><path d="M0 2h12v1L6 7 0 3zM0 4.3l6 4 6-4V10H0z"/></svg>
        <span>info@youremail.com</span>
      </li>
      <li class="contact__item">
        <svg class="contact__icon" viewBox="0 0 12 12"><path d="M6 0a6 6 0 1 0 0 12A6 6 0 1 0 6 0zm0 1.2c0.8 0 1.6 1.5 1.8 4.2H4.2C4.4 2.7 5.2 1.2 6 1.2zM1.2 6.6h1.9c0.1 1.6 0.4 3 0.9 3.9A4.8 4.8 0 0 1 1.2 6.6zm0-1.2A4.8 4.8 0 0 1 4 1.5C3.5 2.4 3.2 3.8 3.1 5.4zm3 1.2h3.6c-0.2 2.7-1 4.2-1.8 4.2s-1.6-1.5-1.8-4.2zm4.7 0h1.9A4.8 4.8 0 0 1 8 10.5c0.5-0.9 0.8-2.3 0.9-3.9zm0-1.2c-0.1-1.6-0.4-3-0.9-3.9a4.8 4.8 0 0 1 2.8 3.9z"/></svg>
        <span>www.youreweb.com</span>
      </li>
    </ul>
    <p class="address"><span class="address__company">Company name</span> - Street Name, Suite 300 State, Zip Code, Country</p>
  </section>
</body>
</html>
```